Redesign of SnapHarbor Lumora Mobile app

The App exists, is up and running but the design is not the best (my creation and i am a developer).
Project landing page http://snapharbor.example/

Also the app has live tiles small, medium and large.

The purpose of this is to have a professional design and make this app the best app on the Lumora Mobile marketplace of his kind.

This app is a picture library that tells you where you've made you're pictures and gives you a unique perspective on the places that you have visited.

If this is successful there will be a version for Lumora 8, Zentrix and QOS also.

The app right now is for LM7 and LM8 and because of this the performance is not the best. With this new design the app will be for LM8 only and have the best performance possible.

I am not sure what else should i mention here but i am glad to answer to any questions if you are interested.

I am using Vantor draft as a design tool and Vantor Mixer and Crafton bench as development tools so if you can provide compatible file the better but is not mandatory.

It wold be nice to keep the existing color palette but again nothing is mandatory I just need a good design.

Links:
App on Marketplace http://www.appdepotmobile.example/en-us/store/app/snapharbor/7a3f9d21-0b6c-4e8d-9f12-ab34cd56ef78

App landing page http://snapharbor.example/
Updates

Reason: The submission time was extended doe to the request of designers.

We can do better, I will increase the budget with 200$  so the total budget will be 480$ so please consider this more seriously.

Thank you.

Target Market(s)

Lumora Mobile users that travel and make pictures.

Industry/Entity Type

Library

Requirements
Must have
• Panorama control as the App main page like in the present.

Representation of visited locations , Live tiles, Map, share location and picture..

If the designer comes up with better proposition they will be take in consideration.

None of these are mandatory but we should keep a connection with the present design so the users will not have the impression that this is a totally different app, this is SnapHarbor but better, more professional.

```html
<!DOCTYPE html>
<html lang="en">
<head>
<meta charset="utf-8">
<title>SnapHarbor – share screens</title>
<link rel="stylesheet" href="https://fonts.googleapis.com/css2?family=Open+Sans:wght@300;400;600&display=swap">
<style>
  :root {
    --page-bg: #ffffff;
    --status-bg: #000000;
    --header-blue: #3b5898;
    --place-blue: #3a5796;
    --message-bg: #8b9cc0;
    --appbar-blue: #0e5ea9;
    --text-white: #ffffff;
    --text-soft: #c9d5ef;
    --address-blue: #b7c7ea;
    --photo-light: #c9d2a0;
    --photo-mid: #7d8f3a;
    --photo-dark: #3f4a1c;
    --avatar-warm: #c9652f;
    --avatar-skin: #e7c0a6;
  }
  * { box-sizing: border-box; margin: 0; padding: 0; }
  html, body {
    width: 1200px; height: 890px; overflow: hidden;
    background: var(--page-bg);
    font-family: "Open Sans", sans-serif;
  }
  .canvas { position: relative; width: 1200px; height: 890px; }
  .screen {
    position: absolute; top: 52px; width: 449px; height: 748px;
    overflow: hidden; background: var(--message-bg);
  }
  .screen--with-place { left: 121px; }
  .screen--compact { left: 606px; }

  .status-bar {
    position: absolute; top: 0; left: 0; width: 100%; height: 30px;
    background: var(--status-bg); color: var(--text-white);
    display: flex; justify-content: flex-end; align-items: center;
    gap: 8px; padding-right: 10px; font-size: 16px;
  }
  .status-bar svg { width: 30px; height: 16px; }

  .profile-header {
    position: absolute; top: 30px; left: 0; width: 100%; height: 182px;
    background: var(--header-blue); color: var(--text-white);
  }
  .app-name {
    position: absolute; left: 14px; top: 10px;
    font-size: 36px; font-weight: 400; letter-spacing: -0.5px;
  }
  .network-name {
    position: absolute; right: 12px; top: 22px;
    font-size: 27px; font-weight: 400;
  }
  .avatar {
    position: absolute; left: 16px; top: 76px; width: 93px; height: 93px;
    border-radius: 50%;
    background: radial-gradient(circle at 55% 50%, var(--avatar-skin) 0%, var(--avatar-warm) 70%);
  }
  .user-name {
    position: absolute; left: 124px; top: 80px;
    font-size: 40px; font-weight: 300; line-height: 1.2;
  }
  .friend-count {
    position: absolute; left: 125px; top: 132px;
    font-size: 16px; font-weight: 400; color: var(--text-soft);
  }

  .photo {
    position: absolute; top: 212px; left: 0; width: 100%; height: 303px;
    background:
      radial-gradient(ellipse 30% 45% at 55% 40%, rgba(238,240,234,0.85) 0%, rgba(238,240,234,0) 100%),
      linear-gradient(180deg, var(--photo-light) 0%, var(--photo-mid) 45%, var(--photo-mid) 70%, var(--photo-dark) 100%);
  }
  .photo-pin {
    position: absolute; top: 477px; left: 0; width: 38px; height: 38px;
    background: var(--place-blue);
    display: flex; align-items: center; justify-content: center;
  }
  .photo-pin svg { width: 18px; height: 24px; }

  .place-bar {
    position: absolute; top: 515px; left: 0; width: 100%; height: 41px;
    background: var(--place-blue);
    display: flex; align-items: center; padding: 0 10px 0 8px;
  }
  .place-bar .pin { width: 18px; height: 24px; margin-right: 5px; }
  .place-label { color: var(--text-white); font-size: 21px; margin-right: 10px; }
  .place-address { color: var(--address-blue); font-size: 17px; flex: 1; white-space: nowrap; }
  .place-check { width: 22px; height: 22px; }

  .message-field {
    position: absolute; left: 0; width: 100%;
    background: var(--message-bg); color: var(--text-white);
    font-size: 21px; padding: 6px 11px;
  }
  .screen--with-place .message-field { top: 556px; height: 126px; }
  .screen--compact .message-field { top: 515px; height: 167px; }

  .app-bar {
    position: absolute; top: 682px; left: 0; width: 100%; height: 66px;
    background: var(--appbar-blue);
  }
  .app-bar__button {
    position: absolute; top: 12px; width: 43px; height: 43px;
  }
  .app-bar__button--send { left: 164px; }
  .app-bar__button--delete { left: 242px; }
  .app-bar__more {
    position: absolute; right: 20px; top: 2px;
    color: var(--text-white); font-size: 22px; letter-spacing: 1px; line-height: 1;
  }
</style>
</head>
<body>
<div class="canvas">

  <svg width="0" height="0" style="position:absolute">
    <defs>
      <symbol id="icon-battery" viewBox="0 0 30 16">
        <rect x="9" y="2" width="18" height="12" rx="1" fill="none" stroke="#fff" stroke-width="2"/>
        <rect x="27" y="5" width="2" height="6" fill="#fff"/>
        <rect x="11" y="4" width="14" height="8" fill="#fff"/>
        <path d="M0 8h6M3 5v6" stroke="#fff" stroke-width="2"/>
      </symbol>
      <symbol id="icon-pin" viewBox="0 0 18 24">
        <path d="M9 1a8 8 0 0 1 8 8c0 6-8 14-8 14S1 15 1 9a8 8 0 0 1 8-8z" fill="none" stroke="#fff" stroke-width="2.2"/>
        <circle cx="9" cy="9" r="3" fill="#fff"/>
      </symbol>
      <symbol id="icon-send" viewBox="0 0 43 43">
        <circle cx="21.5" cy="21.5" r="19.5" fill="none" stroke="#fff" stroke-width="2.5"/>
        <path d="M19 14h13v11h-4l-3 4v-4h-6z" fill="#fff"/>
        <path d="M10 16h7M12 20h5M10 24h7" stroke="#fff" stroke-width="2"/>
      </symbol>
      <symbol id="icon-delete" viewBox="0 0 43 43">
        <circle cx="21.5" cy="21.5" r="19.5" fill="none" stroke="#fff" stroke-width="2.5"/>
        <path d="M14 15h15M19 15v-2h5v2" stroke="#fff" stroke-width="2" fill="none"/>
        <path d="M15.5 17h12l-1 13h-10z" fill="none" stroke="#fff" stroke-width="2"/>
        <path d="M19.5 19.5v8M23.5 19.5v8" stroke="#fff" stroke-width="1.6"/>
      </symbol>
    </defs>
  </svg>

  <section class="screen screen--with-place">
    <div class="status-bar"><svg><use href="#icon-battery"/></svg><span>14:49</span></div>
    <header class="profile-header">
      <div class="app-name">SnapHarbor</div>
      <div class="network-name">friendnet</div>
      <div class="avatar" role="img" aria-label="Profile portrait of the user"></div>
      <div class="user-name">Mara Tellen</div>
      <div class="friend-count">You have 109 friends.</div>
    </header>
    <div class="photo" role="img" aria-label="Photo of a white feather resting on green moss"></div>
    <div class="place-bar">
      <svg class="pin"><use href="#icon-pin"/></svg>
      <span class="place-label">Place:</span>
      <span class="place-address">Harbor Lane 12,00349 Portvale</span>
      <svg class="place-check" viewBox="0 0 22 22">
        <rect x="1" y="1" width="20" height="20" fill="#2d4680" stroke="#fff" stroke-width="1"/>
        <path d="M5 11l4 4 8-9" fill="none" stroke="#fff" stroke-width="2.4"/>
      </svg>
    </div>
    <div class="message-field">Message:</div>
    <nav class="app-bar">
      <svg class="app-bar__button app-bar__button--send"><use href="#icon-send"/></svg>
      <svg class="app-bar__button app-bar__button--delete"><use href="#icon-delete"/></svg>
      <span class="app-bar__more">•••</span>
    </nav>
  </section>

  <section class="screen screen--compact">
    <div class="status-bar"><svg><use href="#icon-battery"/></svg><span>14:49</span></div>
    <header class="profile-header">
      <div class="app-name">SnapHarbor</div>
      <div class="network-name">friendnet</div>
      <div class="avatar" role="img" aria-label="Profile portrait of the user"></div>
      <div class="user-name">Mara Tellen</div>
      <div class="friend-count">You have 109 friends.</div>
    </header>
    <div class="photo" role="img" aria-label="Photo of a white feather resting on green moss"></div>
    <div class="photo-pin"><svg><use href="#icon-pin"/></svg></div>
    <div class="message-field">Message:</div>
    <nav class="app-bar">
      <svg class="app-bar__button app-bar__button--send"><use href="#icon-send"/></svg>
      <svg class="app-bar__button app-bar__button--delete"><use href="#icon-delete"/></svg>
      <span class="app-bar__more">•••</span>
    </nav>
  </section>

</div>
</body>
</html>
```